Amber Burrows Business Card Design

Amber Burrows - Gathering Gentle Meadow Corners

Amber Burrows is a company that focuses on promoting the design, construction, consultation and support of natural, creative and organic play spaces for Early Childhood and learning environments.

We need a professional Business Card designed that is unique modern and creative. The Philosophy of the company is nostalgic so the business and will need to reflect this but also reflect that our ideas are modern and cutting edge.

The business card will need to be a talking point, by either having a unique size, quality and/or placement of logo or other quality.

I am more interested in using natural recycled paper, as this would reflect the philosophy of the company, but I open to seeing colour used creatively.
Updates

Hi Designers, Apologies, Could you please add www.amberburrows.com.au to the business card. Thanks very much.

Hi All, Thank you all for your submission thus far. Please note the fonts for used in the logo are: Ostrich Sans Black and Archer Semi Bold. If these could be considered for contact details, my name etc. Also please show the design on a recycled brown card if possible as this will be the type of card I will use when printing. Thanks so much.

Target Market(s)

Child Care Providers, Play Industry Professionals

Industry/Entity Type

Business

Contact Information for Business Card

Amber Burrows
Gathering Gentle Meadow Corners
Marguerite Holloway
0419 862 503
marguerite@amberburrows.com.au

Font styles to use
Sans Serif

Requirements
Must have
• The Logo and the Details plus the below phrase
• Amber Burrows - Gathering Gentle Meadow Corners
Nice to have
• A bit of colour, but not too much colour.
Should not have
• Not to have a white background, recycled brown card only

```html
<!DOCTYPE html>
<html lang="en">
<head>
<meta charset="utf-8">
<title>Amber Burrows Business Card Design</title>
<link rel="stylesheet" href="https://fonts.googleapis.com/css2?family=Open+Sans:wght@400;700&family=Arvo:wght@400;700&display=swap">
<style>
  :root {
    --backdrop: #e4e4e6;
    --kraft: #c9a57f;
    --kraft-deep: #b8926a;
    --ink: #1e1a16;
    --emboss: #a98660;
  }
  html, body {
    margin: 0;
    width: 1200px;
    height: 1000px;
    overflow: hidden;
    background: var(--backdrop);
  }
  .canvas {
    position: relative;
    width: 1200px;
    height: 1000px;
  }
  .card {
    position: absolute;
    left: 265px;
    width: 667px;
    height: 397px;
    background: var(--kraft);
    box-shadow: 0 6px 12px rgba(0,0,0,0.25);
  }
  .card-front { top: 73px; }
  .card-back { top: 532px; }

  .brand {
    position: absolute;
    left: 20px;
    width: 363px;
    text-align: center;
  }
  .brand-mark {
    display: block;
    margin: 0 auto;
    width: 92px;
    height: 92px;
    border-radius: 50%;
    background: var(--ink);
  }
  .brand-name {
    margin: 14px 0 0;
    font-family: "Open Sans", sans-serif;
    font-weight: 700;
    font-size: 40px;
    letter-spacing: 1px;
    line-height: 1;
    text-transform: uppercase;
    color: var(--ink);
  }
  .brand-tagline {
    margin: 8px 0 0;
    font-family: "Arvo", serif;
    font-size: 14px;
    line-height: 1.3;
    text-transform: uppercase;
    color: var(--ink);
  }
  .card-front .brand { top: 98px; }

  .card-back .brand { left: 152px; top: 68px; }
  .card-back .brand-mark { width: 128px; height: 128px; background: var(--kraft-deep); }
  .card-back .brand-name { font-size: 46px; margin-top: 60px; color: var(--emboss); }
  .card-back .brand-tagline { font-size: 16px; color: var(--emboss); }

  .contact {
    position: absolute;
    left: 370px;
    top: 126px;
    font-family: "Open Sans", sans-serif;
    color: var(--ink);
  }
  .contact-name {
    margin: 0 0 46px;
    font-weight: 700;
    font-size: 17px;
    letter-spacing: 0.5px;
    text-transform: uppercase;
  }
  .contact-list {
    list-style: none;
    margin: 0;
    padding: 0;
    font-size: 15px;
  }
  .contact-list li {
    display: flex;
    align-items: center;
    gap: 8px;
    height: 26px;
  }
  .contact-list svg { width: 13px; height: 13px; fill: var(--ink); flex: none; }
</style>
</head>
<body>
<div class="canvas">
  <section class="card card-front">
    <div class="brand">
      <span class="brand-mark" aria-hidden="true"></span>
      <h1 class="brand-name">Amber Burrows</h1>
      <p class="brand-tagline">Gathering<br>Gentle Meadow Corners</p>
    </div>
    <div class="contact">
      <h2 class="contact-name">Marguerite Holloway</h2>
      <ul class="contact-list">
        <li>
          <svg viewBox="0 0 16 16" aria-hidden="true"><path d="M3 1h3l1.5 4-2 1.2a9 9 0 0 0 4.3 4.3L11 8.5l4 1.5v3a2 2 0 0 1-2 2C6.9 15 1 9.1 1 3a2 2 0 0 1 2-2z"/></svg>
          0419 862 503
        </li>
        <li>
          <svg viewBox="0 0 16 16" aria-hidden="true"><path d="M1 3h14v10H1z M1 3l7 6 7-6" stroke="#c9a57f" stroke-width="1.2"/></svg>
          marguerite@amberburrows.com.au
        </li>
        <li>
          <svg viewBox="0 0 16 16" aria-hidden="true"><circle cx="8" cy="8" r="7"/><path d="M1 8h14M8 1c-3 3.5-3 10.5 0 14M8 1c3 3.5 3 10.5 0 14" stroke="#c9a57f" stroke-width="1" fill="none"/></svg>
          www.amberburrows.com.au
        </li>
      </ul>
    </div>
  </section>

  <section class="card card-back">
    <div class="brand">
      <span class="brand-mark" aria-hidden="true"></span>
      <p class="brand-name">Amber Burrows</p>
      <p class="brand-tagline">Gathering<br>Gentle Meadow Corners</p>
    </div>
  </section>
</div>
</body>
</html>
```